Review/Re-Design Supermarket E-Commerce website

We have launched our Supermarket E-commerce Website but feel it is lacking a modern feel.

Please re-design the current Supermarket E-commerce site, creating a more modern look and feel.

I am looking for design changes to things such as:

- Fonts
- Button shape & Size
- Shapes of boxes
- Layout of drop down menus
- A new shopping cart / button
- The Header (and in particular the use and positioning of the logo)
- Supplying a generic background image (currently berries)

Please do not change the structure of the page. For instance, the category selection will always be on the left, the items will always be displayed in rows of 3 and the shopping cart should be on the right.
Updates

Current site can be found at www.brovanmarket.com.au

Project Deadline Extended
Reason: designs coming in are generally too different from current design. we are looking for less that 10% change to the overall look and feel. one aspect that needs a lot of work is the checkout cart on the right hand side. please checkout http://www2.pelkinfreshmart.com.au/?gclid=QXRP4kdmwnLBHTYEzJuaPGEKtB

Target Market(s)

Consumers buying their weekly grocery shopping online

Industry/Entity Type

Shopping

Number of Pages Required

1 page

Requirements
Must have
• Stick to the branding of the Logo. Which is Red, Blue and White.
• Other colours may be used in small percentages.
Should not have
• Do not change the Structure of the site.

```html
<!DOCTYPE html>
<html lang="en">
<head>
<meta charset="utf-8">
<title>Brovan Market Supermarkets – Online Specials</title>
<link rel="stylesheet" href="https://fonts.googleapis.com/css2?family=Source+Sans+3:ital,wght@0,400;0,600;0,700;1,400;1,700&family=Arimo&display=swap">
<style>
:root{
  --brand-blue:#0a63b0;
  --link-blue:#1d6fb8;
  --navy:#18325a;
  --brand-red:#ee1c3a;
  --green:#5fae2e;
  --green-light:#7cc040;
  --yellow:#ffd400;
  --grey-band:#f1f0ee;
  --border:#d6d6d6;
  --text:#333;
  --muted:#666;
  --qty-bg:#d9e9f5;
  --search-btn:#79aee0;
}
*{box-sizing:border-box;margin:0;padding:0}
html,body{width:1200px;height:918px;overflow:hidden;background:#fff}
body{position:relative;font-family:"Source Sans 3",Arial,sans-serif;color:var(--text)}
.abs{position:absolute}
.top-bar{left:0;top:0;width:1200px;height:8px;background:var(--brand-blue)}
.bottom-bar{left:0;top:909px;width:1200px;height:9px;background:var(--brand-blue)}

.brand{left:31px;top:40px;display:flex;align-items:center;gap:12px}
.brand-name{font-size:30px;font-weight:700;color:var(--brand-blue);letter-spacing:.5px;line-height:1}
.brand-name small{display:block;font-size:19px;letter-spacing:4.5px;margin-top:2px;font-weight:700}
.brand-dot{width:46px;height:46px;border-radius:50%;background:var(--brand-red)}

.main-nav{right:24px;top:8px;display:flex;height:36px;font-size:17px}
.main-nav a{display:flex;align-items:center;padding:0 13px;color:var(--navy);text-decoration:none}
.main-nav .register{background:var(--green);color:#fff;width:82px;justify-content:center;margin-left:0}
.main-nav .login{background:var(--brand-blue);color:#fff;width:68px;justify-content:center;margin-left:2px}
.info-line{right:28px;top:66px;font-size:18px;font-style:italic;color:var(--link-blue)}
.info-line b{font-weight:700}

.search-band{left:0;top:110px;width:1200px;height:57px;background:var(--grey-band)}
.search-input{left:19px;top:123px;width:497px;height:32px;background:#fff;border:1px solid #cfcfcf}
.search-btn{left:515px;top:123px;width:76px;height:32px;background:var(--search-btn);display:flex;align-items:center;justify-content:center}
.tool-btn{top:122px;width:143px;height:33px;background:#fff;border:1px solid #cfcfcf;font-family:Arimo,Arial,sans-serif;font-size:12px;color:#333;display:flex;align-items:center;justify-content:center}

.breadcrumb{left:19px;top:184px;font-size:16px;color:var(--link-blue)}
.breadcrumb .home{color:var(--green)}

.side-tab{left:20px;width:177px;height:31px;display:flex;align-items:center;gap:6px;padding-left:9px;font-size:16px}
.tab-fav{top:232px;background:var(--yellow);color:#444}
.tab-specials{top:264px;background:var(--brand-red);color:#fff}
.category-list{left:20px;top:303px;width:177px;list-style:none}
.category-list li{height:22.2px;border-bottom:1px solid #cfcfcf;font-size:12px;color:#444;display:flex;align-items:center;padding-left:14px;position:relative}
.category-list li::before{content:"";position:absolute;left:20px;border-left:4px solid var(--brand-red);border-top:3px solid transparent;border-bottom:3px solid transparent}
.category-list li{padding-left:32px}
.category-list li.active{background:#ececec;font-weight:700}
.category-list li.sub{padding-left:48px}
.category-list li.sub::before{left:35px;border-left-color:var(--link-blue)}

.product-card{width:218px;height:308px;border:1px solid var(--border);background:#fff}
.product-photo{position:absolute;left:20px;top:18px;width:176px;height:170px;border-radius:50%}
.photo-red{background:radial-gradient(circle at 50% 55%,#c8464a 0,#b8474c 38%,#e9c9c3 56%,#fff 72%)}
.photo-green{background:radial-gradient(circle at 50% 58%,#7cc51f 0,#5ea814 38%,#d2ecb6 56%,#fff 72%)}
.product-name{position:absolute;left:13px;top:219px;font-size:12px;color:#555}
.product-price{position:absolute;left:13px;top:241px;font-size:18px;color:#333;display:flex;align-items:center}
.product-price .sep{width:2px;height:19px;background:#333;margin:0 10px}
.product-price small{font-size:12px}
.qty{position:absolute;left:3px;top:270px;width:122px;height:36px;background:var(--qty-bg);display:flex;align-items:center;justify-content:space-between;padding:0 11px;font-size:15px}
.qty-btn{width:16px;height:16px;border-radius:50%;background:#222;color:#fff;font-size:13px;line-height:16px;text-align:center;font-weight:700}
.add-btn{position:absolute;left:129px;top:270px;width:85px;height:36px;background:var(--green);color:#fff;font-size:15px;display:flex;align-items:center;justify-content:center}

.info-panel{left:937px;top:232px;width:218px;height:155px;border:1px solid var(--border)}
.info-row{position:absolute;left:14px;display:flex;gap:9px;align-items:flex-start}
.info-icon{width:58px;height:58px;border-radius:50%;display:flex;align-items:center;justify-content:center;flex:none}
.icon-pink{background:#f26a7e}
.icon-green{background:var(--green)}
.info-text{padding-top:8px;font-size:9.5px;line-height:1.2;color:#222;width:115px}
.info-text strong{display:block;font-size:12px;color:#2c8fd6;font-weight:700;margin-bottom:2px}

.cart-panel{left:937px;top:400px;width:218px;height:156px;border:1px solid var(--border)}
.cart-icon{position:absolute;left:14px;top:18px;width:58px;height:58px;border-radius:50%;background:#2f8ed4;display:flex;align-items:center;justify-content:center}
.cart-count{position:absolute;left:85px;top:16px;width:120px;font-size:12px;padding-bottom:6px;border-bottom:1px solid #cfcfcf}
.cart-count b{font-size:18px;font-weight:400}
.cart-sub{position:absolute;left:85px;top:48px;font-size:12px}
.cart-sub b{display:block;font-size:18px;font-weight:400}
.checkout-btn{position:absolute;left:12px;top:99px;width:190px;height:44px;border-radius:22px;background:var(--brand-red);color:#fff;font-size:15px;display:flex;align-items:center;justify-content:center}
</style>
</head>
<body>
<div class="abs top-bar"></div>

<div class="abs brand">
  <div class="brand-name">BROVAN MARKET<small>SUPERMARKETS</small></div>
  <div class="brand-dot"></div>
</div>

<nav class="abs main-nav">
  <a href="#">My Cart</a>
  <a href="#">Products</a>
  <a href="#" class="register">Register</a>
  <a href="#" class="login">Login</a>
</nav>
<div class="abs info-line">For more info Call Us Now <b>1300 555 204</b></div>

<div class="abs search-band"></div>
<div class="abs search-input"></div>
<div class="abs search-btn">
  <svg width="18" height="18" viewBox="0 0 18 18"><circle cx="7.5" cy="7.5" r="5.5" fill="none" stroke="#fff" stroke-width="2.4"/><line x1="11.5" y1="11.5" x2="16" y2="16" stroke="#fff" stroke-width="2.8" stroke-linecap="round"/></svg>
</div>
<div class="abs tool-btn" style="left:607px">Filter by</div>
<div class="abs tool-btn" style="left:767px">Sort</div>

<div class="abs breadcrumb"><span class="home">Home</span> &nbsp;/ Online Specials &nbsp;/ Online Specials</div>

<div class="abs side-tab tab-fav">
  <svg width="17" height="17" viewBox="0 0 20 20"><path d="M10 1l2.7 5.6 6.1.8-4.5 4.3 1.1 6.1L10 14.9 4.6 17.8l1.1-6.1L1.2 7.4l6.1-.8z" fill="#fff"/></svg>Favourites
</div>
<div class="abs side-tab tab-specials">
  <svg width="20" height="16" viewBox="0 0 20 16"><rect x="3" y="2" width="14" height="9" fill="none" stroke="#fff" stroke-width="1.5"/><rect x="1" y="12" width="18" height="2" fill="#fff"/></svg>Online Specials
</div>

<ul class="abs category-list">
  <li>Fruit</li><li>Vegetables</li><li>Meat</li><li>Serviced Deli</li>
  <li class="active">Bakery</li>
  <li class="sub">Chilled Foods</li><li class="sub">Bacon</li><li class="sub">Fruit</li><li class="sub">Vegetables</li>
  <li>Meat</li><li>Serviced Deli</li><li>Bakery</li><li>Chilled Foods</li><li>Bacon</li>
  <li>Meat</li><li>Serviced Deli</li><li>Bakery</li><li>Chilled Foods</li><li>Bacon</li>
  <li>Meat</li><li>Serviced Deli</li><li>Bakery</li><li>Chilled Foods</li><li>Bacon</li>
</ul>

<!-- product row 1 -->
<div class="abs product-card" style="left:222px;top:232px">
  <div class="product-photo photo-red" role="img" aria-label="Photo of a red apple"></div>
  <div class="product-name">Apples red 2kg bag</div>
  <div class="product-price">$8.39<span class="sep"></span><small>$8.39 ea</small></div>
  <div class="qty"><span class="qty-btn">+</span>1<span class="qty-btn">−</span></div>
  <div class="add-btn">ADD</div>
</div>
<div class="abs product-card" style="left:459px;top:232px">
  <div class="product-photo photo-red" role="img" aria-label="Photo of a red apple"></div>
  <div class="product-name">Apples red 2kg bag</div>
  <div class="product-price">$8.39<span class="sep"></span><small>$8.39 ea</small></div>
  <div class="qty"><span class="qty-btn">+</span>1<span class="qty-btn">−</span></div>
  <div class="add-btn">ADD</div>
</div>
<div class="abs product-card" style="left:696px;top:232px">
  <div class="product-photo photo-red" role="img" aria-label="Photo of a red apple"></div>
  <div class="product-name">Apples red 2kg bag</div>
  <div class="product-price">$8.39<span class="sep"></span><small>$8.39 ea</small></div>
  <div class="qty"><span class="qty-btn">+</span>1<span class="qty-btn">−</span></div>
  <div class="add-btn">ADD</div>
</div>

<!-- product row 2 -->
<div class="abs product-card" style="left:222px;top:561px">
  <div class="product-photo photo-green" role="img" aria-label="Photo of a green apple with a leaf"></div>
  <div class="product-name">Apples red 2kg bag</div>
  <div class="product-price">$8.39<span class="sep"></span><small>$8.39 ea</small></div>
  <div class="qty"><span class="qty-btn">+</span>1<span class="qty-btn">−</span></div>
  <div class="add-btn">ADD</div>
</div>
<div class="abs product-card" style="left:459px;top:561px">
  <div class="product-photo photo-green" role="img" aria-label="Photo of a green apple with a leaf"></div>
  <div class="product-name">Apples red 2kg bag</div>
  <div class="product-price">$8.39<span class="sep"></span><small>$8.39 ea</small></div>
  <div class="qty"><span class="qty-btn">+</span>1<span class="qty-btn">−</span></div>
  <div class="add-btn">ADD</div>
</div>
<div class="abs product-card" style="left:696px;top:561px">
  <div class="product-photo photo-green" role="img" aria-label="Photo of a green apple with a leaf"></div>
  <div class="product-name">Apples red 2kg bag</div>
  <div class="product-price">$8.39<span class="sep"></span><small>$8.39 ea</small></div>
  <div class="qty"><span class="qty-btn">+</span>1<span class="qty-btn">−</span></div>
  <div class="add-btn">ADD</div>
</div>

<aside class="abs info-panel">
  <div class="info-row" style="top:11px">
    <div class="info-icon icon-pink">
      <svg width="30" height="30" viewBox="0 0 30 30"><rect x="5" y="12" width="20" height="15" fill="none" stroke="#fff" stroke-width="2"/><rect x="3" y="8" width="24" height="5" fill="#fff"/><line x1="15" y1="8" x2="15" y2="27" stroke="#f26a7e" stroke-width="2"/></svg>
    </div>
    <div class="info-text"><strong>Click &amp; Collect</strong>4/12-18 Marlow Street Dunmore TAS 7390</div>
  </div>
  <div class="info-row" style="top:80px">
    <div class="info-icon icon-green">
      <svg width="34" height="26" viewBox="0 0 34 26"><rect x="2" y="5" width="19" height="13" fill="#fff"/><path d="M21 9h7l4 5v4H21z" fill="#fff"/><circle cx="9" cy="20" r="3" fill="#fff" stroke="#5fae2e" stroke-width="1.5"/><circle cx="26" cy="20" r="3" fill="#fff" stroke="#5fae2e" stroke-width="1.5"/></svg>
    </div>
    <div class="info-text"><strong>Delivery info</strong>No Delivery Available</div>
  </div>
</aside>

<aside class="abs cart-panel">
  <div class="cart-icon">
    <svg width="32" height="30" viewBox="0 0 32 30"><path d="M2 5h5l4 15h15l3-11H9" fill="none" stroke="#fff" stroke-width="2.2" stroke-linejoin="round"/><circle cx="13" cy="25" r="2.2" fill="#fff"/><circle cx="24" cy="25" r="2.2" fill="#fff"/></svg>
  </div>
  <div class="cart-count"><b>0</b> items</div>
  <div class="cart-sub">Sub Total<b>$0.00</b></div>
  <div class="checkout-btn">CHEKC OUT</div>
</aside>

<div class="abs bottom-bar"></div>
</body>
</html>
```